Laptop Accessories Packing Design

We are looking for a new package design of a laptop accesories (batteries, charges, hard drives etc.). We want to refresh our brand Vireo CellWorks. At VireoCell, we create high-end laptop accessories that ensure reliability, performance, and longevity for users worldwide. Our mission is to deliver innovative and durable solutions that allow users to work, create, and grow without limits.
General Packaging Concept
Minimalist and elegant look, yet with elements that catch the eye (Vireo products will mainly be offered on auction portals such as Brindle, Kiva, Tollmart, so it would be good if the packaging attracted attention and stood out from the competitors).
Should I put a photo, sketch or product icon on the box? We'll leave that to your imagination.
We ask for a general design of the packaging. After the competition, together with the winner, we will add the rest of the information to the back and sides of the box.
In the attachments there is our Logo (you can use other colors) and sample packaging of competitors
Target Market(s)
E-commerse
Industry/Entity Type
individual end customer
Look and feel
Each slider illustrates characteristics of the customer's brand and the style your logo design should communicate.

```html
<!DOCTYPE html>
<html lang="en">
<head>
<meta charset="utf-8">
<title>Vireo CellWorks – Packaging Colourways</title>
<link rel="stylesheet" href="https://fonts.googleapis.com/css2?family=Exo+2:ital,wght@0,400;0,700;0,800;1,700;1,800&family=Teko:wght@500&display=swap">
<style>
  :root{
    --green:#9bbf1d;
    --teal:#2f9495;
    --dark:#1c1c1c;
    --product:#2a2a2a;
    --light:#ffffff;
    --stage:#e3e1de;
  }
  *{box-sizing:border-box;margin:0;padding:0}
  html,body{width:1197px;height:1200px;overflow:hidden}
  body{background:var(--stage);font-family:"Exo 2",sans-serif;color:var(--dark)}

  .colourway{position:relative;width:1197px;height:600px}
  .colourway + .colourway{border-top:1px solid #cfccc8}
  .colourway.green-teal{--base:var(--green);--band:var(--teal);--ink-base:var(--dark);--ink-band:var(--light)}
  .colourway.teal-green{--base:var(--teal);--band:var(--green);--ink-base:var(--light);--ink-band:var(--dark)}

  .swatch-label{position:absolute;right:24px;top:16px;text-align:right}
  .swatch-label .names{font-family:"Teko",sans-serif;font-weight:500;font-size:46px;line-height:.9;letter-spacing:.5px}
  .swatch-label .codes{font-weight:800;font-size:14px;letter-spacing:1.5px}
  .c-green{color:var(--green)} .c-teal{color:var(--teal)}

  .box{position:absolute;overflow:hidden;background:var(--base);box-shadow:0 6px 14px rgba(0,0,0,.18)}
  .band{position:absolute;background:var(--band)}
  .brand{font-weight:800;letter-spacing:-.5px;line-height:1;position:absolute;white-space:nowrap}
  .on-base{color:var(--ink-base)} .on-band{color:var(--ink-band)}
  .product-shot{position:absolute;background:linear-gradient(160deg,#3a3a3a,#141414);border-radius:6px}
  .headline{position:absolute;font-weight:800;font-style:italic;white-space:nowrap;line-height:1}
  .copy{position:absolute;font-size:9px;font-style:italic;line-height:1.25}

  /* battery box */
  .battery{left:40px;top:70px;width:140px;height:500px}
  .battery .band{left:0;bottom:0;width:100%;height:130px}
  .battery .product-shot{left:14px;top:14px;width:60px;height:280px}
  .battery .rot{position:absolute;transform:rotate(-90deg);transform-origin:left top}
  .battery .headline{font-size:26px;left:82px;top:300px;width:240px}
  .battery .volt{font-size:22px;left:110px;top:110px}
  .battery .brand{font-size:36px;left:88px;top:470px}

  /* keyboard box */
  .keyboard{left:210px;top:90px;width:650px;height:240px}
  .keyboard .band.top{left:120px;top:0;right:0;height:62px}
  .keyboard .band.side{left:0;top:62px;width:120px;bottom:0}
  .keyboard .brand{font-size:46px;left:150px;top:84px}
  .keyboard .copy{right:26px;top:80px;text-align:right;width:230px}
  .keyboard .headline{font-size:26px;right:26px;top:106px}
  .keyboard .product-shot{right:18px;top:142px;width:290px;height:88px}
  .keyboard .small-tag{position:absolute;left:150px;top:186px;font-weight:700;font-size:11px;line-height:1.2}
  .keyboard .small-tag b{font-size:13px}

  /* ssd box */
  .ssd{left:890px;top:110px;width:250px;height:290px}
  .ssd .band{left:0;top:0;width:100%;height:100px}
  .ssd .brand{font-size:36px;left:50%;transform:translateX(-50%);top:32px}
  .ssd .headline{font-size:19px;left:20px;top:114px}
  .ssd .rule{position:absolute;left:20px;top:138px;width:170px;height:2px;background:currentColor}
  .ssd .copy{left:20px;top:144px;width:190px}
  .ssd .product-shot{left:40px;top:180px;width:190px;height:100px}

  /* cable hanger box */
  .cable{left:210px;top:360px;width:300px;height:210px}
  .cable .band{left:0;top:0;width:90px;height:100%}
  .cable .hang-hole{position:absolute;left:140px;top:10px;width:40px;height:16px;border-radius:10px;background:var(--dark)}
  .cable .brand{font-size:34px;left:120px;top:38px}
  .cable .product-shot{left:100px;top:84px;width:180px;height:92px;border-radius:4px}
  .cable .headline{font-size:14px;right:14px;bottom:12px}

  /* mouse box */
  .mouse{left:540px;top:390px;width:320px;height:170px;background:var(--band)}
  .mouse .band{left:0;top:0;width:100%;height:62px;background:var(--base)}
  .mouse .product-shot{left:20px;top:10px;width:150px;height:42px;border-radius:20px}
  .mouse .headline{font-size:13px;left:190px;top:24px}
  .mouse .brand{font-size:38px;left:50%;transform:translateX(-50%);top:96px}
</style>
</head>
<body>

<section class="colourway green-teal">
  <div class="swatch-label">
    <div class="names"><span class="c-green">GREEN</span> <span class="c-teal">- TEAL</span></div>
    <div class="codes"><span class="c-green">#9BBF1D</span> - <span class="c-teal">#2F9495</span></div>
  </div>

  <div class="box battery">
    <div class="band"></div>
    <div class="product-shot" role="img" aria-label="Photo of a black laptop battery"></div>
    <div class="rot headline on-base">LOREM IPSUM</div>
    <div class="rot headline volt on-base">14.8V</div>
    <div class="rot brand on-band">Vireo</div>
  </div>

  <div class="box keyboard">
    <div class="band top"></div><div class="band side"></div>
    <div class="brand on-base">Vireo</div>
    <div class="copy on-base">Lorem ipsum dolor sit amet, consectetuer adipiscing elit, sed diam nonummy</div>
    <div class="headline on-base">LOREM IPSUM-128</div>
    <div class="small-tag on-base">LOREM IPSUM<br><b>LOREM IPSUM</b></div>
    <div class="product-shot" role="img" aria-label="Illustration of a laptop keyboard"></div>
  </div>

  <div class="box ssd on-base">
    <div class="band"></div>
    <div class="brand on-band">Vireo</div>
    <div class="headline">SOLID SATA DRIVE</div>
    <div class="rule"></div>
    <div class="copy">Lorem ipsum dolor sit amet, consectetuer adipiscing elit, sed diam</div>
    <div class="product-shot" role="img" aria-label="Illustration of a 500GB solid state drive"></div>
  </div>

  <div class="box cable">
    <div class="band"></div>
    <div class="hang-hole"></div>
    <div class="brand on-base">Vireo</div>
    <div class="product-shot" role="img" aria-label="Window showing a coiled charging cable"></div>
    <div class="headline on-base">LOREM IPSUM</div>
  </div>

  <div class="box mouse">
    <div class="band"></div>
    <div class="product-shot" role="img" aria-label="Photo of a computer mouse"></div>
    <div class="headline on-base">LOREM IPSUM -128</div>
    <div class="brand on-band">Vireo</div>
  </div>
</section>

<section class="colourway teal-green">
  <div class="swatch-label">
    <div class="names"><span class="c-teal">TEAL</span> <span class="c-green">- GREEN</span></div>
    <div class="codes"><span class="c-teal">#2F9495</span> - <span class="c-green">#9BBF1D</span></div>
  </div>

  <div class="box battery">
    <div class="band"></div>
    <div class="product-shot" role="img" aria-label="Photo of a black laptop battery"></div>
    <div class="rot headline on-base">LOREM IPSUM</div>
    <div class="rot headline volt on-base">14.8V</div>
    <div class="rot brand on-band">Vireo</div>
  </div>

  <div class="box keyboard">
    <div class="band top"></div><div class="band side"></div>
    <div class="brand on-base">Vireo</div>
    <div class="copy on-base">Lorem ipsum dolor sit amet, consectetuer adipiscing elit, sed diam nonummy</div>
    <div class="headline on-base">LOREM IPSUM-128</div>
    <div class="small-tag on-base">LOREM IPSUM<br><b>LOREM IPSUM</b></div>
    <div class="product-shot" role="img" aria-label="Illustration of a laptop keyboard"></div>
  </div>

  <div class="box ssd on-base">
    <div class="band"></div>
    <div class="brand on-band">Vireo</div>
    <div class="headline">SOLID SATA DRIVE</div>
    <div class="rule"></div>
    <div class="copy">Lorem ipsum dolor sit amet, consectetuer adipiscing elit, sed diam</div>
    <div class="product-shot" role="img" aria-label="Illustration of a 500GB solid state drive"></div>
  </div>

  <div class="box cable">
    <div class="band"></div>
    <div class="hang-hole"></div>
    <div class="brand on-base">Vireo</div>
    <div class="product-shot" role="img" aria-label="Window showing a coiled charging cable"></div>
    <div class="headline on-base">LOREM IPSUM</div>
  </div>

  <div class="box mouse">
    <div class="band"></div>
    <div class="product-shot" role="img" aria-label="Photo of a computer mouse"></div>
    <div class="headline on-base">LOREM IPSUM -128</div>
    <div class="brand on-band">Vireo</div>
  </div>
</section>

</body>
</html>
```